LUMA Neighborhood Aid for Critter Welfare

LUMA SCS PET OWNERS WITH VACCINATIONS, MICROCHIP, Spay & NEUTER, TRANSPORTATION FOR PET OWNERS THAT ARE ELDERLY OR MOBILITY CHALLENGED, PET SITTING, PET GROOMING, EDUCATION, adoption counseling, grief counseling, in-home evaluations, feral trap and release, public speaking on education of pet ownership, seminars, meetings and outreach. LUMA depends 100% on donations. I need the webpage to be able to link up to my PayPal account for donations. Serving the greater Houston area.

Reason: My dog of 15 yrs is dying.

```html
<!DOCTYPE html>
<html lang="en">
<head>
<meta charset="utf-8">
<title>LUMA – Neighborhood Aid for Critter Welfare</title>
<link href="https://fonts.googleapis.com/css2?family=Open+Sans:ital,wght@0,300;0,400;0,600;1,400&display=swap" rel="stylesheet">
<style>
:root{
  --green:#7ea623;
  --green-dark:#5f7f14;
  --orange:#e0693a;
  --yellow:#f6d22a;
  --cream:#fbf3ea;
  --text:#555;
  --text-light:#888;
  --dark:#3c3c3c;
  --darker:#2d2d2d;
  --white:#fff;
}
*{box-sizing:border-box;margin:0;padding:0}
html,body{width:1200px;height:2715px;overflow:hidden;background:var(--white)}
body{font-family:'Open Sans',sans-serif;color:var(--text);position:relative}
.section-title{font-weight:400;color:var(--orange);font-size:34px;text-align:center}

/* hero + header */
.hero{position:relative;height:642px;background:radial-gradient(ellipse at 45% 55%,#8d8a84 0%,#4a4843 35%,#1c1b19 70%,#0b0b0a 100%)}
.hero-photo{position:absolute;inset:0}
.site-header{position:absolute;left:100px;top:0;width:1000px}
.brand-bar{height:87px;background:var(--green);display:flex;align-items:center;justify-content:space-between;padding:0 18px}
.brand{font-size:52px;font-weight:400;color:var(--white);letter-spacing:1px}
.header-actions{display:flex;gap:8px}
.btn{font-size:15px;font-weight:600;padding:10px 14px;border-radius:2px;color:var(--white);background:var(--green-dark);text-transform:uppercase}
.btn-donate{background:var(--yellow);color:#3a3a1a}
.main-nav{height:51px;background:var(--white);display:flex;align-items:center;padding:0 28px}
.main-nav a{font-size:14px;color:#555;text-decoration:none;text-transform:uppercase;margin-right:34px}
.main-nav a.active{color:var(--orange)}
.nav-search{margin-left:auto;display:flex;align-items:center}
.nav-search span{font-size:13px;color:#bbb;width:130px}
.nav-search .go{width:34px;height:34px;background:#333;display:flex;align-items:center;justify-content:center}
.hero-caption{position:absolute;right:100px;top:245px;text-align:right;font-weight:300}
.hero-caption .line1{color:var(--white);font-size:33px}
.hero-caption .line2{color:var(--yellow);font-size:44px;margin-top:2px}
.slider-dots{position:absolute;left:550px;top:600px;width:101px;height:24px;border-radius:12px;background:#444;display:flex;align-items:center;justify-content:center;gap:9px}
.slider-dots i{width:10px;height:10px;border-radius:50%;border:2px solid #ddd;background:#777}
.slider-dots i.on{background:#eee}

/* welcome */
.welcome{height:258px;padding-top:55px;text-align:center}
.welcome p{width:890px;margin:18px auto 0;font-size:14px;line-height:24px;color:var(--text-light)}

/* services */
.services{height:684px;background:var(--cream);padding-top:46px}
.service-grid{display:grid;grid-template-columns:repeat(4,226px);gap:34px 24px;margin:34px 0 0 109px}
.service-card{height:228px;background:var(--white);box-shadow:0 1px 3px rgba(0,0,0,.12);padding:5px}
.service-photo{height:166px}
.service-card h3{font-weight:400;font-size:21px;color:var(--green);text-align:center;margin-top:12px}
.service-card.donate .service-photo{background:var(--green);display:flex;align-items:center;justify-content:center;text-align:center;color:var(--white);font-weight:600;font-size:17px;line-height:27px;padding:0 20px}

/* testimonials */
.testimonials{height:300px;padding-top:46px;position:relative}
.testimonial{display:flex;margin:30px 0 0 128px;width:960px}
.avatar{width:124px;height:124px;border-radius:50%;border:4px solid var(--white);box-shadow:0 1px 6px rgba(0,0,0,.25);background:radial-gradient(circle at 50% 40%,#d9b9a0 0%,#b89079 45%,#e6e6e6 46%,#f2f2f2 100%);flex:none}
.quote{margin-left:22px;padding-top:12px}
.quote p{font-style:italic;font-size:14px;line-height:25px;color:var(--text-light)}
.quote cite{display:block;font-style:normal;color:var(--green);font-size:14px;margin-top:10px}
.arrow{position:absolute;top:148px}
.arrow.prev{left:38px}.arrow.next{right:38px}
.divider{width:1000px;margin:0 auto;border:0;border-top:1px solid #e4e4e4}

/* news */
.news{height:433px;padding-top:50px}
.news-grid{display:grid;grid-template-columns:repeat(4,230px);gap:20px;margin:32px 0 0 109px}
.news-photo{height:146px}
.news-item p{font-size:15px;line-height:21px;color:#444;margin-top:14px}
.news-item time{display:block;font-size:13px;color:var(--text-light);margin-top:6px}

/* contact */
.contact{height:298px;background:var(--dark);padding-top:34px}
.contact h2{color:var(--white);font-size:20px;font-weight:600;text-align:center}
.contact-form{width:828px;margin:24px auto 0}
.field-row{display:flex;gap:18px}
.field{flex:1;height:35px;border:1px solid #888;border-radius:3px;color:#ccc;font-size:13px;padding:8px 14px}
.field.message{height:67px;margin-top:21px}
.submit{display:block;width:78px;margin:20px auto 0;background:var(--yellow);color:#333;font-weight:600;font-size:15px;padding:6px 0;text-align:center;border-radius:2px}

/* footer */
.site-footer{height:100px;background:var(--darker);position:relative;padding:22px 0 0 100px;color:#bbb;font-size:13px}
.footer-links a{color:#bbb;text-decoration:none}
.footer-links .sep{margin:0 10px}
.copyright{margin-top:12px}
.social{position:absolute;left:854px;top:35px;display:flex;gap:9px}
.social i{width:32px;height:32px;border-radius:50%;background:#6b6b6b}
</style>
</head>
<body>

<section class="hero">
  <div class="hero-photo" role="img" aria-label="Photo of a grey kitten crouching on a floor"></div>
  <header class="site-header">
    <div class="brand-bar">
      <div class="brand">LUMA</div>
      <div class="header-actions">
        <span class="btn btn-donate">Donate Now</span>
        <span class="btn">Register</span>
        <span class="btn">Login</span>
      </div>
    </div>
    <nav class="main-nav">
      <a class="active" href="#">Home</a><a href="#">About Us</a><a href="#">Services</a><a href="#">Products</a><a href="#">News &amp; Events</a><a href="#">Gallery</a><a href="#">Contact Us</a>
      <div class="nav-search"><span>SEARCH</span><div class="go"><svg width="16" height="16" viewBox="0 0 16 16"><circle cx="6.5" cy="6.5" r="4.5" fill="none" stroke="#fff" stroke-width="2"/><line x1="10" y1="10" x2="14" y2="14" stroke="#fff" stroke-width="2"/></svg></div></div>
    </nav>
  </header>
  <div class="hero-caption">
    <div class="line1">We are doing service in</div>
    <div class="line2">Elm Ridge Valley.</div>
  </div>
  <div class="slider-dots"><i class="on"></i><i></i><i></i><i></i></div>
</section>

<section class="welcome">
  <h2 class="section-title">Welcome to LUMA</h2>
  <p>Donec tempus porta tempus. In tincidunt et libero quis pulvinar. Maecenas dapibus odio aliquam ornare convallis. Aliquam iaculis, nisl ut ultricies sodales, mi purus bibendum augue, eget laoreet felis massa sit amet ante. Fusce purus mauris, malesuada et imperdiet vel, mattis eu mauris. Sed dapibus urna magna, a eleifend neque lobortis ac. Etiam viverra dolor non tristique hendrerit. Suspendisse iaculis ligula ac lacus eleifend, eget posuere ante suscipit.</p>
</section>

<section class="services">
  <h2 class="section-title">Our Services</h2>
  <div class="service-grid">
    <div class="service-card"><div class="service-photo" role="img" aria-label="Photo of a vet vaccinating a dog" style="background:linear-gradient(135deg,#7a5a3c,#c9c3bb)"></div><h3>Vaccinations</h3></div>
    <div class="service-card"><div class="service-photo" role="img" aria-label="Photo of a cat being microchipped" style="background:linear-gradient(135deg,#e9e3da,#c99a62)"></div><h3>Microchip</h3></div>
    <div class="service-card"><div class="service-photo" role="img" aria-label="Photo of a shepherd dog" style="background:linear-gradient(135deg,#2e2a22,#7a6a48)"></div><h3>Spay &amp; Neuter</h3></div>
    <div class="service-card"><div class="service-photo" role="img" aria-label="Photo of a woman sitting with a dog" style="background:linear-gradient(135deg,#f1ece6,#b08a66)"></div><h3>Pet Sitting</h3></div>
    <div class="service-card"><div class="service-photo" role="img" aria-label="Photo of a small dog with hair curlers" style="background:linear-gradient(135deg,#dfe8ef,#5c9ccf)"></div><h3>Pet Grooming</h3></div>
    <div class="service-card"><div class="service-photo" role="img" aria-label="Photo of a woman reading with a cat" style="background:linear-gradient(135deg,#d9d2cb,#8e7e74)"></div><h3>Education</h3></div>
    <div class="service-card"><div class="service-photo" role="img" aria-label="Photo of dogs looking out of a car" style="background:linear-gradient(160deg,#4d7fb8,#b98a5c)"></div><h3>Transportation</h3></div>
    <div class="service-card donate"><div class="service-photo">PELLENTESQUE TEMPUS MAURIS UT MAGNA PLACERAT MOLLIS</div><h3>Donate Now</h3></div>
  </div>
</section>

<section class="testimonials">
  <h2 class="section-title">Testimonials</h2>
  <div class="testimonial">
    <div class="avatar" role="img" aria-label="Portrait photo of the reviewer"></div>
    <div class="quote">
      <p>“ Nam a malesuada libero. Duis sodales et libero vel interdum. Interdum et malesuada fames ac ante ipsum primis in faucibus. Donec lobortis dui tortor, eu lobortis felis mattis nec. Sed justo quam, luctus eu mauris eget, euismod dapibus sem. Sed tempus feugiat ante, at ornare libero volutpat sed. Maecenas quis magna magna. ”</p>
      <cite>Dorian - City</cite>
    </div>
  </div>
  <svg class="arrow prev" width="20" height="32" viewBox="0 0 20 32"><polyline points="16,2 4,16 16,30" fill="none" stroke="#bbb" stroke-width="3"/></svg>
  <svg class="arrow next" width="20" height="32" viewBox="0 0 20 32"><polyline points="4,2 16,16 4,30" fill="none" stroke="#bbb" stroke-width="3"/></svg>
</section>
<hr class="divider">

<section class="news">
  <h2 class="section-title">Latest News</h2>
  <div class="news-grid">
    <article class="news-item"><div class="news-photo" role="img" aria-label="Image of two hands reaching out with a caption about helping others" style="background:linear-gradient(135deg,#e0a12c,#b9661c)"></div><p>Suspendisse iaculis ligula ac lacus eleifend, eget posuere ante suscipit.</p><time>Aug - 15 - 2014</time></article>
    <article class="news-item"><div class="news-photo" role="img" aria-label="Photo of two cats in a cardboard box" style="background:linear-gradient(135deg,#a98661,#5a4a3c)"></div><p>Suspendisse iaculis ligula ac lacus eleifend, eget posuere ante suscipit.</p><time>Aug - 15 - 2014</time></article>
    <article class="news-item"><div class="news-photo" role="img" aria-label="Image of a dog with a quote about dogs" style="background:linear-gradient(135deg,#3a3f45,#1d2126)"></div><p>Suspendisse iaculis ligula ac lacus eleifend, eget posuere ante suscipit.</p><time>Aug - 15 - 2014</time></article>
    <article class="news-item"><div class="news-photo" role="img" aria-label="Image of a lion with a quote about courage" style="background:linear-gradient(135deg,#2b2014,#8a5a2a)"></div><p>Suspendisse iaculis ligula ac lacus eleifend, eget posuere ante suscipit.</p><time>Aug - 15 - 2014</time></article>
  </div>
</section>

<section class="contact">
  <h2>Contact Us</h2>
  <div class="contact-form">
    <div class="field-row"><div class="field">Name</div><div class="field">E-mail</div><div class="field">Phone</div></div>
    <div class="field message">Message</div>
    <span class="submit">SUBMIT</span>
  </div>
</section>

<footer class="site-footer">
  <div class="footer-links"><a href="#">Home</a><span class="sep">|</span><a href="#">About us</a><span class="sep">|</span><a href="#">Services</a><span class="sep">|</span><a href="#">Products</a><span class="sep">|</span><a href="#">News &amp; Events</a><span class="sep">|</span><a href="#">Gallery</a><span class="sep">|</span><a href="#">Contact us</a><span class="sep">|</span><a href="#">Search</a></div>
  <div class="copyright">Copyright &nbsp;©&nbsp; 2014 &nbsp;LUMA. &nbsp; All rights reserved.</div>
  <div class="social"><i></i><i></i><i></i><i></i><i></i><i></i></div>
</footer>

</body>
</html>
```